Quirky Paris documentary film needs a poster

I'm making a quirky documentary about how I've seen too many romantic comedies so I've moved to Paris to try to turn my life into a rom-com. It's called "A Foreign Teapot On Holiday." I've included a few sample stills, or the whole thing could be an illustration. The film is full of references to other films like Odette, Thursday By Lantern, Lucinda, so you could riff of of their posters. 27" x 41"

Industry/Entity Type

Film Production

Font styles to use
Sans Serif

Requirements
Must have
• It should say "From the director of Finding Nutmeg" "Brontemor Films Presents" "Directed by Dale R. Whitcomb" and at the bottom it should have the website: aforeignteapotonholiday.example
Nice to have
• You could possibly include this text:
• What happens when you've seen too many romantic comedies?
• You move to Paris and try to turn your life into one.

```html
<!DOCTYPE html>
<html lang="en">
<head>
<meta charset="utf-8">
<title>A Foreign Teapot On Holiday — Poster</title>
<link rel="stylesheet" href="https://fonts.googleapis.com/css2?family=Amatic+SC:wght@700&family=Oswald:wght@500&display=swap">
<style>
  :root{
    --sky-top:#94cfdf;
    --sky-mid:#c6e6ee;
    --sky-bottom:#f4fafc;
    --cloud:rgba(255,255,255,0.55);
    --rose:#e8354a;
    --ink:#26343a;
    --credit-ink:#1d1d1d;
    --hair:#d9773a;
    --shirt:#e9eccf;
  }
  html,body{margin:0;padding:0;overflow:hidden;}
  .poster{
    position:relative;width:790px;height:1200px;overflow:hidden;
    background:linear-gradient(180deg,var(--sky-top) 0%,var(--sky-mid) 45%,var(--sky-bottom) 100%);
    font-family:"Oswald",sans-serif;color:var(--ink);
  }
  .cloud{position:absolute;}
  .credits{
    position:absolute;top:62px;left:0;width:790px;text-align:center;
    font-size:21px;letter-spacing:0.2px;line-height:32px;text-transform:uppercase;
  }
  .title{
    margin:0;
    font-family:"Amatic SC",sans-serif;font-weight:700;color:var(--rose);text-transform:uppercase;
  }
  .title-row{position:absolute;display:flex;align-items:center;white-space:nowrap;}
  .title-row--one{top:150px;left:130px;}
  .title-row--two{top:292px;left:118px;}
  .title-small{
    font-size:52px;line-height:1;padding-bottom:4px;margin-right:14px;
    border-bottom:3px solid var(--rose);
  }
  .title-big{font-size:124px;line-height:0.95;}
  .director{
    margin-left:26px;
    font-family:"Amatic SC",sans-serif;font-weight:700;color:var(--credit-ink);
    font-size:46px;line-height:46px;text-transform:uppercase;white-space:nowrap;
  }
  .portrait{position:absolute;left:0;top:448px;}
  .tagline{
    position:absolute;left:462px;top:552px;width:300px;
    font-family:"Amatic SC",sans-serif;font-weight:700;color:var(--rose);text-transform:uppercase;
    font-size:31px;line-height:34px;
  }
  .tagline p{margin:0 0 32px 0;padding-left:18px;text-indent:-18px;}
  .tagline p::before{content:"- ";}
  .site{
    position:absolute;left:460px;top:890px;width:284px;
    border-top:3px solid var(--ink);border-bottom:3px solid var(--ink);
    border-radius:2px;padding:13px 0 14px;text-align:center;
    font-size:17.5px;text-transform:uppercase;letter-spacing:0.1px;
  }
</style>
</head>
<body>
<main class="poster">
  <svg class="cloud" style="left:0;top:0" width="790" height="480" role="img" aria-label="Hand-drawn white outline clouds drifting across the sky">
    <ellipse cx="300" cy="20" rx="120" ry="40" fill="var(--cloud)"/>
    <ellipse cx="690" cy="120" rx="110" ry="95" fill="var(--cloud)"/>
    <ellipse cx="90" cy="215" rx="110" ry="65" fill="var(--cloud)"/>
    <ellipse cx="700" cy="390" rx="100" ry="65" fill="var(--cloud)"/>
  </svg>

  <header class="credits">
    <div>From the director of Finding Nutmeg</div>
    <div>Brontemor Films Presents</div>
  </header>

  <h1 class="title">
    <span class="title-row title-row--one">
      <span class="title-small">A</span><span class="title-big">Foreign Teapot</span>
    </span>
    <span class="title-row title-row--two">
      <span class="title-small">On</span><span class="title-big">Holiday</span>
      <span class="director">Directed by<br>Dale R. Whitcomb</span>
    </span>
  </h1>

  <svg class="portrait" width="440" height="752" role="img" aria-label="Photo of a smiling red-haired man in red heart-shaped sunglasses and a tropical print shirt">
    <defs>
      <linearGradient id="portrait-tone" x1="0" y1="0" x2="0" y2="1">
        <stop offset="0" stop-color="var(--hair)"/>
        <stop offset="0.2" stop-color="#e6b79a"/>
        <stop offset="0.75" stop-color="#dca98c"/>
        <stop offset="0.85" stop-color="var(--shirt)"/>
      </linearGradient>
    </defs>
    <path d="M70 60 Q220 -20 380 80 Q440 240 400 450 Q360 560 330 610 L440 700 L440 752 L0 752 L0 620 Q30 560 40 450 Q0 250 70 60 Z" fill="url(#portrait-tone)"/>
  </svg>

  <section class="tagline">
    <p>What happens when you've seen too many romantic comedies?</p>
    <p>You move to Paris and try to turn your life into one.</p>
    <p>What could possibly go wrong?</p>
  </section>

  <div class="site">aforeignteapotonholiday.example</div>
</main>
</body>
</html>
```